Not another boring Business Card Design Project

This is not another boring Business Card Design Project.

We are looking for the weirdest, wackiest most boundary pushing designs that you can come up with.

If you believe that design can be fun, energetic, crazy, unpredictable, beautiful and eye-catching then read on… this project is for you.

We are Tolvin Presk and we print plastic cards.

We are running a Plastic Card Design Competition.

And we need a plastic card to advertise the competition to graphic designers just like you.

The design needs to make your average designers’ jaws drop and their eyes pop out.

You can do what you wish with the card design, so long as it stands out.

We like these designs, designs that stretch the boundaries and become something beyond just another business card:

http://quorvamedia.net/wp-content/uploads/2009/03/b48.jpg
Designer - http://www.pelvanworks.com/

http://quorvamedia.net/wp-content/uploads/2009/03/b41.jpg
Designer - http://renolbrakstad.com/

http://images.plinthhive.com/designs/44195_732292_37774_thumbnail.jpg
Designer- Zentro Media at Plinth Hive

http://images.plinthhive.com/designs/44195_717529_37774_thumbnail.jpg
Designer - Zentro Media at Plinth Hive

http://quorvamedia.net/wp-content/uploads/2009/03/b11.jpg
Designer - http://www.wk7studio.com/

http://quorvamedia.net/wp-content/uploads/2009/03/b16.jpg
Designer - http://www.pebbletumbler.com/

Reason: A number of designers have said they want to submit designs and haven't yet done so, we want to give them time.

Reason: We've extended the deadline by 4 days for those who want to submit their designs over the weekend and give ourselves time to judge them

Plastic

• The design needs to contain this link: lnk.example/QzRpLk and any other detail that will encourage competition entry. The design will be printed on plastic.
• No borders (when plastic cards are punched to shape and size there is movement of 1 - 2mm, borders highlight this movement).

Keep text 3mm away from edges of the cards.

Please don't create designs to be produced on clear/transparent plastic.

```html
<!DOCTYPE html>
<html lang="en">
<head>
<meta charset="utf-8">
<title>Plastic Card Competition – Side B</title>
<link rel="stylesheet" href="https://fonts.googleapis.com/css2?family=Nunito:wght@900&family=Arimo:wght@400&display=swap">
<style>
  :root {
    --page-bg: #ffffff;
    --stripe-purple: #ac4c85;
    --stripe-navy: #0079bf;
    --stripe-sky: #00a0e1;
    --stripe-green: #009a46;
    --stripe-yellow: #ffec00;
    --stripe-orange: #ee7f1d;
    --stripe-red: #e11f26;
    --link-text: #ffffff;
    --label-text: #2b2b2b;
  }
  html, body {
    margin: 0;
    padding: 0;
    width: 1200px;
    height: 900px;
    overflow: hidden;
    background: var(--page-bg);
  }
  .sheet {
    display: block;
    width: 1200px;
    height: 900px;
  }
  .card-link {
    font-family: "Nunito", "Varela Round", sans-serif;
    font-weight: 900;
    fill: var(--link-text);
  }
  .card-link--hero { font-size: 92px; }
  .card-link--corner { font-size: 38px; }
  .side-label {
    font-family: "Arimo", Arial, sans-serif;
    font-size: 40px;
    fill: var(--label-text);
  }
  .stripe--purple { fill: var(--stripe-purple); }
  .stripe--navy { fill: var(--stripe-navy); }
  .stripe--sky { fill: var(--stripe-sky); }
  .stripe--green { fill: var(--stripe-green); }
  .stripe--yellow { fill: var(--stripe-yellow); }
  .stripe--orange { fill: var(--stripe-orange); }
  .stripe--red { fill: var(--stripe-red); }
</style>
</head>
<body>
<svg class="sheet" viewBox="0 0 1200 900" xmlns="http://www.w3.org/2000/svg">
  <defs>
    <clipPath id="card-shape">
      <rect x="92" y="131" width="1016" height="638" rx="42" ry="42"/>
    </clipPath>
  </defs>

  <g class="card" clip-path="url(#card-shape)">
    <rect class="stripe stripe--purple" x="92" y="131" width="1016" height="91"/>
    <rect class="stripe stripe--navy" x="92" y="221" width="1016" height="92"/>
    <rect class="stripe stripe--sky" x="92" y="312" width="1016" height="90"/>
    <rect class="stripe stripe--green" x="92" y="401" width="1016" height="91"/>
    <rect class="stripe stripe--yellow" x="92" y="491" width="1016" height="91"/>
    <rect class="stripe stripe--orange" x="92" y="581" width="1016" height="91"/>
    <rect class="stripe stripe--red" x="92" y="671" width="1016" height="98"/>

    <text class="card-link card-link--corner" x="147" y="216">lnk.example/QzRpLk</text>
    <text class="card-link card-link--hero" x="600" y="488" text-anchor="middle" textLength="880" lengthAdjust="spacing">lnk.example/QzRpLk</text>
    <text class="card-link card-link--corner" x="1056" y="706" text-anchor="end">lnk.example/QzRpLk</text>
  </g>

  <text class="side-label" x="1158" y="858" text-anchor="end">side B</text>
</svg>
</body>
</html>
```